Mobile Friendly Lead Generation Landing Page

We are a web marketing company that specialized in web lead generation. Recently we have started buying media from mobile devices and we need a mobile interface(landing page) where we can collect user data in an effective manner.

Our current mobile landing page is:
http://www.tuitionscout.example.com/lp13d/index.aspx?a=true&source=581406
Through this you can see what the steps/questions users need to answer to get matched to a school. We need the design for the whole process.

We are pretty open for design ideas and our goal is to make this mobile optimized landing page have the look and feel of an app...but not an app.
There are several questions in the process but we are open to changing the way they are presented. As in, you can have one question at a time or a few.
The goal is to make this EXTREMELY EASY for users to interact with.

One example that we have liked is:
http://lessonhub.example/schools/47215-page1.lhub (please note that this opens only on mobile devices)

Some of these screenshots are attached.

Our web form looks like this:
http://www.tuitionscout.example.com/lp88/index.aspx?a=true

```html
<!DOCTYPE html>
<html lang="en">
<head>
<meta charset="utf-8">
<title>TuitionScout Main Screen</title>
<link rel="stylesheet" href="https://fonts.googleapis.com/css2?family=Roboto+Condensed:wght@300;400;700&family=Roboto:wght@400;500&display=swap">
<style>
  :root {
    --bg: #eef3ee;
    --chrome-blue: #1a9bf0;
    --field-blue: #7cc8f7;
    --strip-blue: #cde9f9;
    --banner-blue: #bfe2f7;
    --title-blue: #1f6fe0;
    --alert-red: #ee1c1c;
    --ribbon-yellow: #fbc02d;
    --ribbon-dark: #e0a31a;
    --row-line: #d9d9d9;
    --text-dark: #1d1d1d;
    --go-green: #17b530;
    --toolbar-blue: #1673f0;
    --ic-pink: #ec1e79;
    --ic-green: #1fb93c;
    --ic-red: #e81d1d;
    --ic-blue: #1b66e8;
    --ic-orange: #f57a1e;
    --ic-black: #111111;
    --white: #ffffff;
  }
  * { box-sizing: border-box; margin: 0; padding: 0; }
  html, body { width: 1200px; height: 840px; overflow: hidden; }
  body {
    background: var(--bg);
    font-family: "Roboto Condensed", "Arial Narrow", sans-serif;
    position: relative;
  }
  .screen {
    position: absolute;
    left: 376px;
    top: 22px;
    width: 320px;
    height: 568px;
    transform: scale(1.4);
    transform-origin: 0 0;
    background: var(--white);
    overflow: hidden;
    box-shadow: 0 2px 6px rgba(0,0,0,.15);
  }
  .browser-top { background: var(--chrome-blue); height: 64px; position: relative; }
  .status-bar {
    height: 20px; display: flex; align-items: center; justify-content: space-between;
    padding: 0 6px; color: var(--white); font-family: "Roboto", sans-serif; font-size: 11px;
  }
  .status-left { display: flex; align-items: center; gap: 4px; }
  .address-field {
    position: absolute; left: 10px; right: 10px; top: 27px; height: 28px;
    background: var(--field-blue); border-radius: 6px;
    display: flex; align-items: center; justify-content: center;
    color: var(--white); font-family: "Roboto", sans-serif; font-size: 14px;
  }
  .address-field svg { position: absolute; right: 8px; top: 6px; }
  .top-strip { height: 14px; background: var(--strip-blue); }
  .headline {
    height: 45px; display: flex; align-items: center; justify-content: center;
    color: var(--title-blue); font-size: 19px; font-weight: 300;
  }
  .headline strong { font-weight: 700; }
  .grant-banner { height: 88px; background: var(--banner-blue); position: relative; }
  .grant-banner svg { position: absolute; inset: 0; }
  .grant-text {
    position: absolute; left: 60px; width: 200px; top: 29px; text-align: center;
    color: var(--white); font-size: 12.5px; line-height: 17px; font-weight: 300;
  }
  .section-title {
    height: 42px; background: var(--alert-red); color: var(--white);
    display: flex; align-items: center; justify-content: center;
    font-size: 17px; font-weight: 300; letter-spacing: .2px;
  }
  .interest-list { list-style: none; }
  .interest-item {
    height: 44px; display: flex; align-items: center; padding: 0 10px 0 8px;
    border-bottom: 1px solid var(--row-line); color: var(--text-dark); font-size: 14px;
  }
  .interest-icon {
    width: 34px; height: 34px; border-radius: 50%; display: flex;
    align-items: center; justify-content: center; margin-right: 9px; flex: none;
  }
  .interest-label { flex: 1; }
  .go { flex: none; }
  .icon-art { background: var(--ic-pink); }
  .icon-business { background: var(--ic-green); }
  .icon-justice { background: var(--ic-red); }
  .icon-education { background: var(--ic-blue); }
  .icon-engineering { background: var(--ic-orange); }
  .icon-other { background: var(--ic-black); }
  .abc {
    color: var(--white); font-family: "Roboto", sans-serif; font-size: 9px; line-height: 9px;
    text-align: center; border: 1px solid var(--white); padding: 1px 2px;
  }
  .toolbar {
    position: absolute; left: 0; right: 0; bottom: 0; height: 51px;
    background: var(--toolbar-blue); display: flex; align-items: center;
    justify-content: space-around;
  }
</style>
</head>
<body>
<main class="screen">
  <header class="browser-top">
    <div class="status-bar">
      <span class="status-left">
        <svg width="28" height="6" viewBox="0 0 28 6"><g fill="#fff"><circle cx="3" cy="3" r="2.5"/><circle cx="9" cy="3" r="2.5"/><circle cx="15" cy="3" r="2.5"/></g><g fill="none" stroke="#fff"><circle cx="21" cy="3" r="2.2"/><circle cx="27" cy="3" r="2.2"/></g></svg>
        <span>Northwave</span>
        <svg width="14" height="10" viewBox="0 0 14 10"><path d="M1 4a9 9 0 0 1 12 0M3.5 6.5a5.5 5.5 0 0 1 7 0" fill="none" stroke="#fff" stroke-width="1.4"/><circle cx="7" cy="9" r="1.2" fill="#fff"/></svg>
      </span>
      <span>4:21 PM</span>
      <span class="status-left">100%
        <svg width="24" height="10" viewBox="0 0 24 10"><rect x=".5" y=".5" width="20" height="9" rx="2" fill="none" stroke="#fff"/><rect x="2" y="2" width="17" height="6" fill="#fff"/><rect x="21.5" y="3" width="2" height="4" fill="#fff"/></svg>
      </span>
    </div>
    <div class="address-field">www.tuitionscout.example.com
      <svg width="16" height="16" viewBox="0 0 16 16"><path d="M13 8a5 5 0 1 1-1.5-3.6M13 2v3h-3" fill="none" stroke="#fff" stroke-width="1.5"/></svg>
    </div>
  </header>
  <div class="top-strip"></div>
  <h1 class="headline">Complete our&nbsp;<strong>3 minute</strong>&nbsp;App!</h1>
  <section class="grant-banner">
    <svg width="320" height="88" viewBox="0 0 320 88">
      <path d="M18 25h46v40H18l10-20z" fill="var(--ribbon-yellow)"/>
      <path d="M302 25h-46v40h46l-10-20z" fill="var(--ribbon-yellow)"/>
      <path d="M22 28h40M22 62h40M298 28h-40M298 62h-40" stroke="#fff" stroke-width="1.2" stroke-dasharray="3 2"/>
      <rect x="54" y="10" width="212" height="66" rx="7" fill="var(--ribbon-yellow)" stroke="var(--ribbon-dark)"/>
      <rect x="61" y="17" width="198" height="52" rx="4" fill="none" stroke="#fff" stroke-width="1.3" stroke-dasharray="4 3"/>
    </svg>
    <p class="grant-text">Get up to $5, 645* per year<br>in Grants if you qualify</p>
  </section>
  <h2 class="section-title">SELECT AREA OF YOUR INTEREST</h2>
  <ul class="interest-list">
    <li class="interest-item">
      <span class="interest-icon icon-art"><svg width="20" height="20" viewBox="0 0 20 20"><path d="M17 2L8 12M8 12c-2-1-4 0-4 2s-1 3-2 4c3 0 6-1 6-4z" fill="none" stroke="#fff" stroke-width="1.4"/></svg></span>
      <span class="interest-label">Art &amp; Design</span>
      <svg class="go" width="20" height="20" viewBox="0 0 20 20"><circle cx="10" cy="10" r="10" fill="var(--go-green)"/><path d="M8 5.5l4.5 4.5L8 14.5" fill="none" stroke="#fff" stroke-width="2.4"/></svg>
    </li>
    <li class="interest-item">
      <span class="interest-icon icon-business"><svg width="20" height="20" viewBox="0 0 20 20"><rect x="2" y="6" width="16" height="11" rx="1" fill="none" stroke="#fff" stroke-width="1.4"/><path d="M7 6V4h6v2M2 10h16M9 10v2h2v-2" fill="none" stroke="#fff" stroke-width="1.4"/></svg></span>
      <span class="interest-label">Business</span>
      <svg class="go" width="20" height="20" viewBox="0 0 20 20"><circle cx="10" cy="10" r="10" fill="var(--go-green)"/><path d="M8 5.5l4.5 4.5L8 14.5" fill="none" stroke="#fff" stroke-width="2.4"/></svg>
    </li>
    <li class="interest-item">
      <span class="interest-icon icon-justice"><svg width="20" height="20" viewBox="0 0 20 20"><rect x="4" y="3" width="9" height="5" transform="rotate(-40 8.5 5.5)" fill="#fff"/><path d="M10 8l6 7" stroke="#fff" stroke-width="2"/><rect x="2" y="15" width="9" height="2.5" fill="#fff"/></svg></span>
      <span class="interest-label">Criminal Justice</span>
      <svg class="go" width="20" height="20" viewBox="0 0 20 20"><circle cx="10" cy="10" r="10" fill="var(--go-green)"/><path d="M8 5.5l4.5 4.5L8 14.5" fill="none" stroke="#fff" stroke-width="2.4"/></svg>
    </li>
    <li class="interest-item">
      <span class="interest-icon icon-education"><span class="abc">ABC<br>1 2 3</span></span>
      <span class="interest-label">Education &amp; Teaching</span>
      <svg class="go" width="20" height="20" viewBox="0 0 20 20"><circle cx="10" cy="10" r="10" fill="var(--go-green)"/><path d="M8 5.5l4.5 4.5L8 14.5" fill="none" stroke="#fff" stroke-width="2.4"/></svg>
    </li>
    <li class="interest-item">
      <span class="interest-icon icon-engineering"><svg width="20" height="20" viewBox="0 0 20 20"><circle cx="10" cy="4" r="1.8" fill="none" stroke="#fff" stroke-width="1.3"/><path d="M9 5.5L4 18M11 5.5L16 18M5 13c3 2 7 2 10 0" fill="none" stroke="#fff" stroke-width="1.3"/></svg></span>
      <span class="interest-label">Engineering</span>
      <svg class="go" width="20" height="20" viewBox="0 0 20 20"><circle cx="10" cy="10" r="10" fill="var(--go-green)"/><path d="M8 5.5l4.5 4.5L8 14.5" fill="none" stroke="#fff" stroke-width="2.4"/></svg>
    </li>
    <li class="interest-item">
      <span class="interest-icon icon-other"><svg width="20" height="20" viewBox="0 0 20 20"><path d="M10 5C7 3 4 3 2 4v11c2-1 5-1 8 1 3-2 6-2 8-1V4c-2-1-5-1-8 1zM10 5v11" fill="none" stroke="#fff" stroke-width="1.3"/></svg></span>
      <span class="interest-label">Other</span>
    </li>
  </ul>
  <nav class="toolbar" aria-label="Browser toolbar">
    <svg width="20" height="24" viewBox="0 0 20 24"><path d="M14 2L4 12l10 10" fill="none" stroke="#fff" stroke-width="1.6"/></svg>
    <svg width="20" height="24" viewBox="0 0 20 24"><path d="M6 2l10 10L6 22" fill="none" stroke="#fff" stroke-width="1.6"/></svg>
    <svg width="24" height="26" viewBox="0 0 24 26"><path d="M8 9H3v15h18V9h-5M12 17V2M7 7l5-5 5 5" fill="none" stroke="#fff" stroke-width="1.5"/></svg>
    <svg width="26" height="22" viewBox="0 0 26 22"><path d="M13 4C9 1 5 1 1 2v18c4-1 8-1 12 1 4-2 8-2 12-1V2c-4-1-8-1-12 2zM13 4v17" fill="none" stroke="#fff" stroke-width="1.5"/></svg>
    <svg width="24" height="24" viewBox="0 0 24 24"><rect x="1" y="6" width="16" height="16" fill="none" stroke="#fff" stroke-width="1.5"/><path d="M5 6V2h16v16h-4" fill="none" stroke="#fff" stroke-width="1.5"/></svg>
  </nav>
</main>
</body>
</html>
```